More Work Available: Menu Design

The total amount available in this contest is $15 AUD.
The total amount of the work I would like to give to the person who wins the contest is a further $35 AUD, making the total of my offer $50.

If no satisfactory entry is submitted within the short period of the contest, then the further work will not be offered.

DESCRIPTION:

The whole ($50) job is a complete menu - many pages.
I will provide you with an excel spreadsheet of the menu - photos and all words.
I have attached an example for you to work off for this contest.

You just need to make it work and look good.

You can make the menu vertical or horizontal.
the way I made the layout is horizontal, square with a fold.

The menu only has about 150 options (including things like zelo, brisol, etc - small things) and could fit on one page but we wish to have many photos so we want to make it over many pages. The attached Excel sheet is 2 pages - cocktails and non alcoholic drinks.

Please make the design simple and elegant - do not use any graphics that have not been provided. simple is best. If you feel like you could waste too much time but are interested in the work - show me a small part of the menu - don't do too much. I know your time is valuable.

```html
<!DOCTYPE html>
<html lang="en">
<head>
<meta charset="utf-8">
<title>Il Forno – Drinks Menu</title>
<link rel="stylesheet" href="https://fonts.googleapis.com/css2?family=Cinzel:wght@700&family=Marcellus+SC&family=Oswald:wght@600&display=swap">
<style>
  :root {
    --ink: #1c1c1c;
    --paper: #ffffff;
    --frame: #d4d4d4;
    --frame-dark: #b9b9b9;
    --peach: #f6c99a;
    --sky: #bfe0f2;
    --lemon: #f7ec9c;
  }
  * { margin: 0; padding: 0; box-sizing: border-box; }
  html, body { width: 1200px; height: 995px; overflow: hidden; background: var(--paper); }
  .menu-page { position: relative; width: 1200px; height: 995px; color: var(--ink); }
  .frames { position: absolute; inset: 0; }
  .menu-title {
    position: absolute; left: 483px; top: 104px;
    font-family: "Oswald", sans-serif; font-weight: 600; font-size: 48px;
    font-variant: small-caps; letter-spacing: 1px; line-height: 1;
  }
  .brand {
    position: absolute; left: 914px; top: 38px; width: 180px; height: 180px;
    display: flex; align-items: center; justify-content: center;
    font-family: "Cinzel", serif; font-weight: 700; font-size: 24px;
    color: var(--ink); text-align: center; line-height: 1.2; letter-spacing: 1px;
  }
  .section-title {
    position: absolute; font-family: "Marcellus SC", serif; font-size: 36px;
    letter-spacing: 1px; line-height: 1;
  }
  .item, .price {
    position: absolute; font-family: "Cinzel", serif; font-weight: 700;
    font-size: 16px; line-height: 1; white-space: nowrap;
  }
  .item { transform: translateX(-50%); }
  .item.small { font-size: 13px; }
  .price { letter-spacing: 2px; }
</style>
</head>
<body>
<main class="menu-page">
  <svg class="frames" width="1200" height="995" viewBox="0 0 1200 995" aria-hidden="true">
    <path d="M488 170 Q600 160 690 168 L684 184 Q590 180 492 186 Z" fill="var(--peach)" opacity=".6"/>
    <path d="M455 262 Q620 255 760 262" stroke="var(--peach)" stroke-width="8" fill="none" opacity=".5"/>
    <path d="M790 488 Q900 480 1010 490" stroke="var(--peach)" stroke-width="9" fill="none" opacity=".5"/>
    <path d="M700 540 Q900 533 1100 542" stroke="var(--sky)" stroke-width="9" fill="none" opacity=".6"/>
    <path d="M452 600 L452 720" stroke="var(--sky)" stroke-width="10" fill="none" opacity=".5"/>
    <path d="M440 792 Q700 782 1110 792" stroke="var(--lemon)" stroke-width="12" fill="none" opacity=".7"/>
    <path d="M700 986 Q900 978 1110 986" stroke="var(--lemon)" stroke-width="8" fill="none" opacity=".7"/>

    <g fill="none" stroke="var(--frame)" stroke-width="8" stroke-linejoin="round">
      <rect x="448" y="68" width="672" height="124"/>
      <rect x="451" y="259" width="668" height="232"/>
      <rect x="446" y="535" width="670" height="200"/>
      <rect x="446" y="786" width="672" height="204"/>
    </g>
    <g fill="none" stroke="var(--frame-dark)" stroke-width="2" opacity=".6">
      <rect x="452" y="72" width="664" height="116"/>
      <rect x="455" y="263" width="660" height="224"/>
      <rect x="450" y="539" width="662" height="192"/>
      <rect x="450" y="790" width="664" height="196"/>
    </g>

    <g stroke="var(--ink)" stroke-width="2.5">
      <line x1="428" y1="120" x2="900" y2="120"/>
      <line x1="428" y1="128" x2="900" y2="128"/>
      <line x1="428" y1="136" x2="900" y2="136"/>
      <line x1="428" y1="144" x2="900" y2="144"/>
    </g>
    <rect x="914" y="60" width="180" height="136" fill="var(--paper)"/>

    <g fill="none" stroke="var(--frame-dark)" stroke-width="4">
      <rect x="764" y="238" width="30" height="30" rx="4"/>
      <rect x="475" y="522" width="30" height="30" rx="4"/>
      <rect x="543" y="770" width="30" height="30" rx="4"/>
    </g>
  </svg>

  <h1 class="menu-title">Menu</h1>
  <div class="brand">IL FORNO<br>ITALIAN GRILL</div>

  <section class="soft-drinks">
    <h2 class="section-title" style="left:806px;top:236px;">soft drinks</h2>
    <span class="item" style="left:555px;top:297px;">Zelo Cola</span><span class="price" style="left:651px;top:297px;">$4.35</span>
    <span class="item" style="left:555px;top:321px;">Zelo Zero</span><span class="price" style="left:651px;top:321px;">$4.35</span>
    <span class="item" style="left:555px;top:346px;">Diet Zelo</span><span class="price" style="left:651px;top:346px;">$4.35</span>
    <span class="item" style="left:555px;top:371px;">Brisol</span><span class="price" style="left:651px;top:371px;">$4.35</span>
    <span class="item" style="left:555px;top:397px;">Fizzo</span><span class="price" style="left:651px;top:397px;">$4.35</span>
    <span class="item" style="left:555px;top:421px;">Sunno</span><span class="price" style="left:651px;top:421px;">$5.35</span>
    <span class="item" style="left:555px;top:444px;">Pink Lemonade</span><span class="price" style="left:651px;top:444px;">$5.35</span>

    <span class="item" style="left:873px;top:326px;">Lemon Lime &amp; Bitters</span><span class="price" style="left:1040px;top:326px;">$5.35</span>
    <span class="item" style="left:873px;top:350px;">San Vitale Limonata</span><span class="price" style="left:1040px;top:350px;">$5.35</span>
    <span class="item" style="left:873px;top:375px;">San Vitale Chinotto</span><span class="price" style="left:1040px;top:375px;">$5.35</span>
    <span class="item small" style="left:873px;top:401px;">San Vitale Aranciata Rossa</span><span class="price" style="left:1040px;top:400px;">$5.35</span>
  </section>

  <section class="iced">
    <h2 class="section-title" style="left:531px;top:520px;">Iced</h2>
    <span class="item" style="left:731px;top:569px;">Iced Coffee</span>
    <span class="item" style="left:731px;top:593px;">Iced Chocolate</span><span class="price" style="left:884px;top:593px;">$7.5</span>
    <span class="item" style="left:731px;top:618px;">Iced Mocha</span><span class="price" style="left:884px;top:618px;">$8.5</span>
    <span class="item" style="left:731px;top:642px;">Peach Iced Tea</span><span class="price" style="left:884px;top:642px;">$6</span>
    <span class="item" style="left:731px;top:667px;">Raspberry Iced Tea</span><span class="price" style="left:884px;top:667px;">$6</span>
    <span class="item" style="left:731px;top:692px;">Lemon Iced Tea</span><span class="price" style="left:884px;top:692px;">$6</span>
  </section>

  <section class="milkshakes-juice">
    <h2 class="section-title" style="left:592px;top:767px;">Milkshakes &amp; Juice</h2>
    <span class="item" style="left:770px;top:816px;">Bottled Pineapple Juice</span><span class="price" style="left:943px;top:816px;">$5.30</span>
    <span class="item" style="left:770px;top:841px;">Freshly Squeezed Orange</span><span class="price" style="left:943px;top:841px;">$7.30</span>
    <span class="item" style="left:770px;top:865px;">Bottled Apple Juice</span><span class="price" style="left:943px;top:865px;">$5.30</span>
    <span class="item" style="left:770px;top:890px;">Chocolate Milkshake</span><span class="price" style="left:943px;top:890px;">$6.30</span>
    <span class="item" style="left:770px;top:915px;">Caramel Milkshake</span><span class="price" style="left:943px;top:915px;">$6.30</span>
    <span class="item" style="left:770px;top:941px;">Strawberry Milkshake</span><span class="price" style="left:943px;top:941px;">$6.30</span>
  </section>
</main>
</body>
</html>
```